" distribuidora no ramo do atacado e varejo (loja fisica ) nos produtos de embalagens em geral (descartáveis, festas e etc.) produtos de limpezas para (residencias , comércios e industriais ) e produtos personalizados no mesmo ramo. "

```html
<!DOCTYPE html>
<html lang="pt-BR">
<head>
<meta charset="UTF-8">
<title>Velmora Distribuidora — Cartão de visita</title>
<link rel="stylesheet" href="https://fonts.googleapis.com/css2?family=Michroma&family=Arimo:wght@400;700&display=swap">
<style>
  :root {
    --bg: #e6e8ea;
    --brand-blue: #1b82ad;
    --brand-blue-deep: #136d94;
    --brand-green: #5fae2e;
    --brand-green-light: #8cc63f;
    --ink-gray: #6d7278;
    --ink-dark: #4a4f55;
    --card-white: #ffffff;
    --logo-font: "Michroma", sans-serif;
    --text-font: "Arimo", sans-serif;
  }
  * { box-sizing: border-box; margin: 0; padding: 0; }
  html, body { width: 1200px; height: 1200px; overflow: hidden; }
  body {
    background: var(--bg);
    font-family: var(--text-font);
    position: relative;
  }
  .card {
    position: absolute;
    left: 150px;
    width: 900px;
    height: 500px;
    overflow: hidden;
    box-shadow: 0 6px 18px rgba(0,0,0,0.12);
  }

  /* Front */
  .card-front {
    top: 80px;
    background: linear-gradient(160deg, var(--brand-blue) 0%, var(--brand-blue-deep) 100%);
  }
  .card-front .accent-band {
    position: absolute; left: 0; right: 0; bottom: 0; height: 22px;
    background: linear-gradient(90deg, var(--brand-green) 0%, var(--brand-green-light) 100%);
  }
  .brand {
    display: flex; flex-direction: column; align-items: center;
  }
  .card-front .brand {
    position: absolute; left: 0; right: 0; top: 110px;
  }
  .brand-mark {
    width: 110px; height: 110px; border-radius: 50%;
    background: var(--brand-green-light);
    margin-bottom: 26px;
  }
  .brand-name {
    font-family: var(--logo-font);
    font-size: 66px;
    letter-spacing: 2px;
    color: #ffffff;
    line-height: 1;
  }
  .brand-tagline {
    font-family: var(--text-font);
    font-size: 20px;
    letter-spacing: 10px;
    color: #ffffff;
    margin-top: 12px;
  }

  /* Back */
  .card-back {
    top: 620px;
    background: var(--card-white);
  }
  .card-back .watermark {
    position: absolute; right: -40px; top: 40px;
    width: 420px; height: 420px; border-radius: 50%;
    background: rgba(27,130,173,0.05);
  }
  .card-back .brand {
    position: absolute; left: 60px; top: 90px; width: 380px;
  }
  .card-back .brand-mark {
    width: 80px; height: 80px; margin-bottom: 18px;
    background: var(--brand-blue);
  }
  .card-back .brand-name { font-size: 42px; color: var(--ink-gray); }
  .card-back .brand-tagline { font-size: 14px; letter-spacing: 7px; color: var(--ink-gray); margin-top: 8px; }

  .contact {
    position: absolute; right: 50px; top: 70px;
    display: flex; flex-direction: column; align-items: flex-end;
    color: var(--ink-dark);
  }
  .person { display: flex; align-items: flex-start; gap: 14px; margin-bottom: 34px; }
  .person-text { text-align: right; }
  .person-name { font-size: 24px; color: var(--brand-blue); letter-spacing: 1px; }
  .person-role { font-size: 12px; color: var(--ink-gray); letter-spacing: 1px; margin-top: 4px; }
  .contact-line {
    display: flex; align-items: center; gap: 14px;
    font-size: 20px; margin-bottom: 22px;
  }
  .icon { width: 22px; height: 22px; flex: none; }
  .icon path, .icon rect, .icon circle { fill: none; stroke: var(--brand-blue); stroke-width: 2; }
  .icon .solid { fill: var(--brand-blue); stroke: none; }

  .card-back .base-band {
    position: absolute; left: 0; right: 0; bottom: 0; height: 26px;
    background: var(--brand-blue);
  }
  .card-back .base-line {
    position: absolute; left: 0; right: 0; bottom: 26px; height: 4px;
    background: var(--brand-green-light);
  }
</style>
</head>
<body>

<section class="card card-front" aria-label="Frente do cartão">
  <div class="brand">
    <div class="brand-mark"></div>
    <div class="brand-name">VELMORA</div>
    <div class="brand-tagline">DISTRIBUIDORA</div>
  </div>
  <div class="accent-band"></div>
</section>

<section class="card card-back" aria-label="Verso do cartão">
  <div class="watermark"></div>
  <div class="brand">
    <div class="brand-mark"></div>
    <div class="brand-name">VELMORA</div>
    <div class="brand-tagline">DISTRIBUIDORA</div>
  </div>

  <div class="contact">
    <div class="person">
      <div class="person-text">
        <div class="person-name">NOME SOBRENOME</div>
        <div class="person-role">CARGO/FUNÇÃO</div>
      </div>
      <svg class="icon" viewBox="0 0 22 22" aria-hidden="true">
        <rect class="solid" x="1" y="1" width="20" height="20" rx="3"/>
        <circle cx="11" cy="8" r="3.5" style="fill:#fff;stroke:none"/>
        <path d="M4.5 18c1-4 12-4 13 0" style="fill:#fff;stroke:none"/>
      </svg>
    </div>
    <div class="contact-line">
      <span>nome@empresa.com.br</span>
      <svg class="icon" viewBox="0 0 22 22" aria-hidden="true">
        <rect x="2" y="5" width="18" height="12" rx="1"/>
        <path d="M2 5l9 7 9-7"/>
      </svg>
    </div>
    <div class="contact-line">
      <span>99 9999-0000</span>
      <svg class="icon" viewBox="0 0 22 22" aria-hidden="true">
        <rect x="3" y="3" width="16" height="16" rx="2"/>
        <path d="M7 7h8M7 11h8M7 15h5"/>
      </svg>
    </div>
    <div class="contact-line">
      <span>99 99999-9999</span>
      <svg class="icon" viewBox="0 0 22 22" aria-hidden="true">
        <rect x="6" y="2" width="10" height="18" rx="2"/>
        <circle cx="11" cy="16.5" r="0.8"/>
      </svg>
    </div>
    <div class="contact-line">
      <span>Rua do Projeto, 999</span>
      <svg class="icon" viewBox="0 0 22 22" aria-hidden="true">
        <path class="solid" d="M11 1C7 1 4 4 4 8c0 5 7 13 7 13s7-8 7-13c0-4-3-7-7-7z"/>
        <circle cx="11" cy="8" r="2.5" style="fill:#fff;stroke:none"/>
      </svg>
    </div>
  </div>

  <div class="base-line"></div>
  <div class="base-band"></div>
</section>

</body>
</html>
```